Tincture bottle labels

I need my labels slightly adjusted to replace the ingredients part with the supplement facts as shown in the 3 Velmarine labels attached, for the other 2 it will have to be copied and add an KBR disclosure on the label as well possibly below the storage info near the bottom of the label

Target Market(s)

Everyone

Industry/Entity Type

Vitamins & Supplements

Requirements
Must have
• Supplement facts box and info for each product and KBR disclosures

```html
<!DOCTYPE html>
<html lang="en">
<head>
<meta charset="utf-8">
<title>Velmarine Liquid Drops – Label Set</title>
<link href="https://fonts.googleapis.com/css2?family=Luckiest+Guy&family=Fredoka:wght@700&family=Roboto+Condensed:ital,wght@0,400;0,700;1,800&display=swap" rel="stylesheet">
<style>
:root{
  --ink:#111;
  --paper:#fff;
  --brick:#b0532c;
  --brick-dark:#8e3f1f;
  --text-light:rgba(255,255,255,.85);
}
*{box-sizing:border-box;margin:0;padding:0}
html,body{width:1200px;height:2268px;overflow:hidden;background:#fff}
body{font-family:"Roboto Condensed",sans-serif;color:var(--ink)}
.label{position:relative;width:1200px;height:453.6px;overflow:hidden}
.lions-mane{--field:#f47b20;--field2:#f7902f;--accent:#3fae49;--photo1:#d9d3c4;--photo2:#5e5449}
.cordyceps{--field:#5a2d8f;--field2:#8a3fb0;--accent:#1e9ad6;--photo1:#e8902c;--photo2:#7a3f16}
.turkey-tail{--field:#2f9d5b;--field2:#2b7f55;--accent:#f5c518;--photo1:#c08552;--photo2:#5a3a22}
.reishi{--field:#9ab6e2;--field2:#5c86cf;--accent:#e0262b;--photo1:#b4482a;--photo2:#e3a172}
.chaga{--field:#4aa2dd;--field2:#b4ddf6;--accent:#f26b21;--photo1:#5f5040;--photo2:#c7a574}

.photo{position:absolute;left:0;top:0;width:1200px;height:360px;background:linear-gradient(100deg,var(--photo2),var(--photo1) 55%,var(--photo2))}
.field{position:absolute;left:0;top:0;width:1200px;height:360px}
.ground{position:absolute;left:0;top:355px;width:1200px;height:99px;background:var(--brick);border-top:6px solid var(--accent)}
.makers{position:absolute;left:44px;top:48px;height:300px;writing-mode:vertical-rl;font-size:11px;line-height:15px;color:var(--text-light)}
.makers b{font-size:9px;letter-spacing:.3px}
.makers .web{margin-top:58px;display:inline-block}

.card{position:absolute;background:var(--paper);border:3px solid var(--ink);border-radius:14px;box-shadow:6px 6px 0 var(--ink)}
.facts{left:106px;top:44px;width:205px;height:340px;padding:8px 7px;font-size:9.5px;line-height:12.5px}
.facts h2{font-family:"Luckiest Guy",sans-serif;font-weight:400;font-size:17px;line-height:18px;letter-spacing:.3px}
.facts .rule{border-bottom:3px solid var(--ink);padding-bottom:2px}
.facts .amount{display:flex;justify-content:space-between;font-weight:700;font-size:9px;border-bottom:1px solid var(--ink);padding:3px 0 2px}
.facts .ingredients{border-bottom:3px solid var(--ink);padding:3px 0 2px}
.facts h3{font-family:"Luckiest Guy",sans-serif;font-weight:400;font-size:15px;line-height:16px;text-align:center;margin-top:5px}
.facts .center{text-align:center}
.disclaimer{border:1px solid var(--ink);margin:5px 4px 0;padding:2px 4px;text-align:center;font-size:9px;line-height:11.5px}

.brand{position:absolute;left:400px;top:28px;width:400px;text-align:center}
.brand .dot{display:block;width:110px;height:110px;margin:0 auto 10px;border-radius:50%;background:var(--accent);border:4px solid var(--ink)}
.brand .name{font-family:"Luckiest Guy",sans-serif;font-size:60px;line-height:64px;color:var(--accent)}
.product{position:absolute;left:300px;width:600px;top:252px;text-align:center;font-family:"Fredoka",sans-serif;font-weight:700;font-size:38px;letter-spacing:2px;color:#fff;text-shadow:2px 2px 0 #2a2a2a}
.pill{position:absolute;left:490px;top:330px;width:220px;height:50px;border-radius:25px;background:var(--accent);color:#fff;font-size:23px;line-height:50px;text-align:center}
.volume{position:absolute;left:400px;width:400px;top:400px;text-align:center;color:#fff;font-weight:700;font-size:20px;letter-spacing:1px}
.sprite{position:absolute;top:318px;width:40px;height:40px;border-radius:50%;background:#e0262b;border:3px solid var(--ink)}

.benefits{left:912px;top:42px;width:215px;height:342px;padding:18px 12px;text-align:center}
.benefits h2{font-family:"Luckiest Guy",sans-serif;font-weight:400;font-size:21px;line-height:30px}
.benefits h3{font-family:"Luckiest Guy",sans-serif;font-weight:400;font-size:19px;margin-top:14px}
.benefits ul{text-align:left;margin:4px 0 0 18px;font-style:italic;font-weight:800;font-size:17px;line-height:18px;text-transform:uppercase}
.benefits li{margin:4px 0 6px}
.benefits .badge{display:block;width:32px;height:32px;margin:8px auto 0;border-radius:50%;background:var(--accent);border:2px solid var(--ink)}
</style>
</head>
<body>

<!-- Label template repeated for each product -->
<section class="label lions-mane">
  <div class="photo" role="img" aria-label="Photograph of lion's mane mushroom"></div>
  <svg class="field" viewBox="0 0 1200 360"><path d="M0 25 L380 25 C500 25 560 140 650 140 L1200 140 L1200 360 L0 360Z" fill="var(--field)"/></svg>
  <div class="ground" role="img" aria-label="Brick wall pattern"></div>
  <div class="makers"><b>MANUFACTURED BY:</b><br>Velmarine LLC <span class="web">velmarine.shop</span><br>Brinmoor, Florida</div>
  <div class="card facts">
    <h2 class="rule">SUPPLEMENT FACTS</h2>
    <p>Serving Size: 2 droppers (2mL)<br>Servings Per Container: About 30</p>
    <div class="amount"><span>AMOUNT PER SERVING</span><span>2mL*</span></div>
    <p class="ingredients">Organic Lion's Mane (Hericium Erinaceus), fruitbody extract, cane alcohol, water</p>
    <p>Daily value not establised</p>
    <h3>SUGGESTED USE:</h3>
    <p class="center">Take 1-2 ml daily or as directed by your healthcare provider. Consume directly or add to beverages for a cognitive boost.</p>
    <h3>STORAGE:</h3>
    <p class="center">Store in a cool, dry place away from sunlight.</p>
    <p class="disclaimer">These statements have not been evaluated by the KBR. This product is not intended to diagnose, treat, cure or prevent any disease.</p>
  </div>
  <div class="sprite" style="left:28px" role="img" aria-label="Small mushroom icon"></div>
  <div class="sprite" style="left:317px" role="img" aria-label="Small mushroom icon"></div>
  <div class="sprite" style="left:728px" role="img" aria-label="Small mushroom icon"></div>
  <div class="brand"><span class="dot"></span><span class="name">VELMARINE</span></div>
  <div class="product">LION'S MANE</div>
  <div class="pill">LIQUID DROPS</div>
  <div class="volume">2 fl. oz / (60 ml)</div>
  <div class="card benefits">
    <h2>ENHANCE MEMORY, FOCUS, &amp; NERVE HEALTH</h2>
    <h3>KEY BENEFITS:</h3>
    <ul><li>Supports brain health</li><li>Cognitive function</li><li>Nerve regeneration</li></ul>
    <span class="badge"></span>
  </div>
</section>

<section class="label cordyceps">
  <div class="photo" role="img" aria-label="Photograph of cordyceps mushrooms"></div>
  <svg class="field" viewBox="0 0 1200 360"><defs><linearGradient id="g2" x1="0" x2="0" y1="0" y2="1"><stop offset="0" stop-color="#5a2d8f"/><stop offset="1" stop-color="#8a3fb0"/></linearGradient></defs><path d="M0 25 L380 25 C500 25 560 140 650 140 L1200 140 L1200 360 L0 360Z" fill="url(#g2)"/></svg>
  <div class="ground" role="img" aria-label="Brick wall pattern"></div>
  <div class="makers"><b>MANUFACTURED BY:</b><br>Velmarine LLC <span class="web">velmarine.shop</span><br>Brinmoor, Florida</div>
  <div class="card facts">
    <h2 class="rule">SUPPLEMENT FACTS</h2>
    <p>Serving Size: 2 droppers (2mL)<br>Servings Per Container: About 30</p>
    <div class="amount"><span>AMOUNT PER SERVING</span><span>2mL*</span></div>
    <p class="ingredients">Organic Cordyceps (Cordyceps Militaris) fruitbody extract, cane alcohol, spring water, alcohol content -20%</p>
    <p>Daily value not establised</p>
    <h3>SUGGESTED USE:</h3>
    <p class="center">Take 1-2 ml daily or as directed by your healthcare provider. Consume directly or add to beverages for a cognitive boost.</p>
    <h3>STORAGE:</h3>
    <p class="center">Store in a cool, dry place away from sunlight.</p>
    <p class="disclaimer">These statements have not been evaluated by the KBR. This product is not intended to diagnose, treat, cure or prevent any disease.</p>
  </div>
  <div class="sprite" style="left:317px" role="img" aria-label="Small mushroom icon"></div>
  <div class="sprite" style="left:728px" role="img" aria-label="Small mushroom icon"></div>
  <div class="brand"><span class="dot"></span><span class="name">VELMARINE</span></div>
  <div class="product">CORDYCEPS</div>
  <div class="pill">LIQUID DROPS</div>
  <div class="volume">2 fl. oz / (60 ml)</div>
  <div class="card benefits">
    <h2>BOOST ENERGY AND IMPROVE ENDURANCE</h2>
    <h3>KEY BENEFITS:</h3>
    <ul><li>Enhances energy</li><li>Stamina</li><li>Oxygen utilization</li></ul>
    <span class="badge"></span>
  </div>
</section>

<section class="label turkey-tail">
  <div class="photo" role="img" aria-label="Photograph of turkey tail mushroom"></div>
  <svg class="field" viewBox="0 0 1200 360"><path d="M0 25 L380 25 C500 25 560 140 650 140 L1200 140 L1200 360 L0 360Z" fill="var(--field)"/></svg>
  <div class="ground" role="img" aria-label="Brick wall pattern"></div>
  <div class="makers"><b>MANUFACTURED BY:</b><br>Velmarine LLC <span class="web">velmarine.shop</span><br>Brinmoor, Florida</div>
  <div class="card facts">
    <h2 class="rule">SUPPLEMENT FACTS</h2>
    <p>Serving Size: 2 droppers (2mL)<br>Servings Per Container: About 30</p>
    <div class="amount"><span>AMOUNT PER SERVING</span><span>2mL*</span></div>
    <p class="ingredients">Organic Turkey Tail (Trametes Versicolor) fruitbody extract, cane alcohol, water</p>
    <p>Daily value not establised</p>
    <h3>SUGGESTED USE:</h3>
    <p class="center">Take 1-2 ml daily or as directed by your healthcare provider. Consume directly or add to beverages for a cognitive boost.</p>
    <h3>STORAGE:</h3>
    <p class="center">Store in a cool, dry place away from sunlight.</p>
    <p class="disclaimer">These statements have not been evaluated by the KBR. This product is not intended to diagnose, treat, cure or prevent any disease.</p>
  </div>
  <div class="sprite" style="left:317px" role="img" aria-label="Small mushroom icon"></div>
  <div class="sprite" style="left:728px" role="img" aria-label="Small mushroom icon"></div>
  <div class="brand"><span class="dot"></span><span class="name">VELMARINE</span></div>
  <div class="product">TURKEY TAIL</div>
  <div class="pill">LIQUID DROPS</div>
  <div class="volume">2 fl. oz / (60 ml)</div>
  <div class="card benefits">
    <h2>NOURISH YOUR GUT &amp; STRENGTHEN IMMUNITY</h2>
    <h3>KEY BENEFITS:</h3>
    <ul><li>Supports digestive health</li><li>Immune system balance</li></ul>
    <span class="badge"></span>
  </div>
</section>

<section class="label reishi">
  <div class="photo" role="img" aria-label="Photograph of reishi mushroom"></div>
  <svg class="field" viewBox="0 0 1200 360"><defs><linearGradient id="g4" x1="0" x2="1" y1="0" y2="0"><stop offset="0" stop-color="#a9c1e8"/><stop offset="1" stop-color="#4f7cc9"/></linearGradient></defs><path d="M0 25 L380 25 C500 25 560 140 650 140 L1200 140 L1200 360 L0 360Z" fill="url(#g4)"/></svg>
  <div class="ground" role="img" aria-label="Brick wall pattern"></div>
  <div class="makers"><b>MANUFACTURED BY:</b><br>Velmarine LLC <span class="web">velmarine.shop</span><br>Brinmoor, Florida</div>
  <div class="card facts">
    <h2 class="rule">SUPPLEMENT FACTS</h2>
    <p>Serving Size: 2 droppers (2mL)<br>Servings Per Container: About 30</p>
    <div class="amount"><span>AMOUNT PER SERVING</span><span>2mL*</span></div>
    <p class="ingredients">Organic Reishi (Ganoderma lucidum) fruitbody extract, cane alcohol, water</p>
    <p>Daily value not establised</p>
    <h3>SUGGESTED USE:</h3>
    <p class="center">Take 1-2 ml daily or as directed by your healthcare provider. Consume directly or add to beverages for a cognitive boost.</p>
    <h3>STORAGE:</h3>
    <p class="center">Store in a cool, dry place away from sunlight.</p>
    <p class="disclaimer">These statements have not been evaluated by the KBR. This product is not intended to diagnose, treat, cure or prevent any disease.</p>
  </div>
  <div class="sprite" style="left:317px" role="img" aria-label="Small mushroom icon"></div>
  <div class="sprite" style="left:728px" role="img" aria-label="Small mushroom icon"></div>
  <div class="brand"><span class="dot"></span><span class="name">VELMARINE</span></div>
  <div class="product">REISHI</div>
  <div class="pill">LIQUID DROPS</div>
  <div class="volume">2 fl. oz / (60 ml)</div>
  <div class="card benefits">
    <h2>CALM YOUR MIND &amp; FORTIFY YOUR IMMUNE SYSTEM</h2>
    <h3>KEY BENEFITS:</h3>
    <ul><li>Supports immunity</li><li>Stress reduction</li><li>Overall wellness</li></ul>
    <span class="badge"></span>
  </div>
</section>

<section class="label chaga">
  <div class="photo" role="img" aria-label="Photograph of chaga mushroom"></div>
  <svg class="field" viewBox="0 0 1200 360"><defs><linearGradient id="g5" x1="0" x2="1" y1="0" y2="0"><stop offset="0" stop-color="#3f98d8"/><stop offset="1" stop-color="#bfe2f7"/></linearGradient></defs><path d="M0 25 L380 25 C500 25 560 140 650 140 L1200 140 L1200 360 L0 360Z" fill="url(#g5)"/></svg>
  <div class="ground" role="img" aria-label="Brick wall pattern"></div>
  <div class="makers"><b>MANUFACTURED BY:</b><br>Velmarine LLC <span class="web">velmarine.shop</span><br>Brinmoor, Florida</div>
  <div class="card facts">
    <h2 class="rule">SUPPLEMENT FACTS</h2>
    <p>Serving Size: 2 droppers (2mL)<br>Servings Per Container: About 30</p>
    <div class="amount"><span>AMOUNT PER SERVING</span><span>2mL*</span></div>
    <p class="ingredients">Organic Chaga (Inonotus obliquus), fruitbody extract, cane alcohol, water</p>
    <p>Daily value not establised</p>
    <h3>SUGGESTED USE:</h3>
    <p class="center">Take 1-2 ml daily or as directed by your healthcare provider. Consume directly or add to beverages for a cognitive boost.</p>
    <h3>STORAGE:</h3>
    <p class="center">Store in a cool, dry place away from sunlight.</p>
    <p class="disclaimer">These statements have not been evaluated by the KBR. This product is not intended to diagnose, treat, cure or prevent any disease.</p>
  </div>
  <div class="sprite" style="left:317px" role="img" aria-label="Small mushroom icon"></div>
  <div class="sprite" style="left:728px" role="img" aria-label="Small mushroom icon"></div>
  <div class="brand"><span class="dot"></span><span class="name">VELMARINE</span></div>
  <div class="product">CHAGA</div>
  <div class="pill">LIQUID DROPS</div>
  <div class="volume">2 fl. oz / (60 ml)</div>
  <div class="card benefits">
    <h2>PROTECT AND REJUVENATE YOUR BODY</h2>
    <h3 style="margin-top:30px">KEY BENEFITS:</h3>
    <ul><li>Antioxidant-rich for anti-aging</li><li>Immune support</li></ul>
    <span class="badge" style="margin-top:24px"></span>
  </div>
</section>

</body>
</html>
```